UK Online Escort Directory Requires a Redesigned Email Marketing Campaign (4 emails total)

These emails should be designed as marketing emails that will be sent out to approx 10,000 potential customers on a by monthly basis. The designs should be innovative, professional designs that are capable of capturing a readers attention in the blink of an eye.

We have posted this job as our in-house design capabilities are not able to create professional email designs, we therefore require a designer to redesign our email marketing campaign (4 emails total) to a professional level.

The content of the emails will be provided, along with the 5 emails that we are currently sending and the company logo. This should give the potential designer all that they need to redesign the campaign to a professional level.

Please see attached brief for more information on what is required from each individual email.

Target Market(s)

Escorts throughout the UK

Industry/Entity Type

Escort

Font styles to use
Serif
Sans Serif

Requirements
Must have
• Instant recognition of what's being offered.
Nice to have
• Imaginative / inspirational designs.
Should not have
• Any unnecessary wording or text.

```html
<!DOCTYPE html>
<html lang="en">
<head>
<meta charset="utf-8">
<title>Velvet Listings – Email Campaign</title>
<link rel="stylesheet" href="https://fonts.googleapis.com/css2?family=Open+Sans:ital,wght@0,400;0,600;0,700;1,400;1,700&display=swap">
<style>
:root{
  --page:#d9c7d8;
  --panel:#ffffff;
  --accent:#8c3f84;
  --logo:#c7a6dc;
  --ink:#333333;
  --muted:#666666;
  --rule:#dddddd;
  --box:#f4f4f4;
  --star:#f29a1f;
  --orange:#ee8a1c;
  --icon:#111111;
}
*{box-sizing:border-box;margin:0;padding:0}
html,body{width:1200px;height:2620px;overflow:hidden}
body{background:var(--page);font-family:"Open Sans",Arial,sans-serif;color:var(--ink);position:relative;line-height:1.4}
.email{position:absolute;left:80px;width:1040px;background:var(--panel);border-top:8px solid var(--accent);padding:24px 80px 28px;text-align:center;overflow:hidden}
.social{display:flex;justify-content:center;gap:14px;margin-bottom:16px}
.social span{width:32px;height:32px;border-radius:50%;background:var(--icon)}
.brand{font-size:58px;font-weight:400;color:var(--logo);letter-spacing:1px;line-height:1;text-align:left;padding-left:120px}
.brand-sub{font-size:18px;color:var(--accent);font-weight:600;text-align:left;padding-left:120px;margin:6px 0 20px}
.lead{font-size:20px;color:var(--muted);margin-bottom:22px}
.listing{display:flex;gap:22px;text-align:left;border:2px solid var(--rule);background:var(--box);padding:20px;margin:0 60px 22px}
.photo{flex:none;border-radius:50%;background:radial-gradient(circle at 40% 35%,#f2d6a8,#c99a6a 60%,#8a6a55)}
.listing .photo{width:130px;height:130px}
.name{font-size:28px;font-weight:700;color:var(--ink);line-height:1.3}
.name small{font-size:19px;font-weight:400;font-style:italic;color:var(--muted);margin-left:8px}
.desc{font-size:17px;color:var(--muted);line-height:1.4;margin:6px 0 8px}
.rec{font-size:17px;font-weight:700;display:flex;align-items:center;gap:10px}
.stars{display:flex;gap:4px}
.stars svg{width:26px;height:26px;fill:var(--star)}
.links{font-size:20px;color:var(--ink);line-height:1.6;text-align:left;padding-left:120px}
.links b{font-style:italic;text-decoration:underline}
.note{position:absolute;top:612px;width:1200px;text-align:center;font-size:19px;color:#4a3a4a}
.note u{color:var(--accent)}
.bar{border:2px solid var(--rule);background:var(--box);font-size:20px;padding:18px;margin:0 60px 24px;text-align:left}
.pair{display:flex;gap:24px;margin:0 60px 30px}
.pair .bar{flex:1;margin:0;font-size:18px;line-height:1.4;min-height:110px}
.offers{display:flex;gap:30px;margin:0 0 30px;align-items:flex-end}
.offer{flex:1}
.offer h3{font-size:17px;font-style:italic;font-weight:700;margin-bottom:12px;min-height:48px;display:flex;align-items:flex-end;justify-content:center}
.mini{display:flex;gap:14px;text-align:left;border:2px solid var(--rule);background:var(--box);padding:14px}
.mini .photo{width:80px;height:80px}
.mini .name{font-size:19px}
.mini .name small{font-size:14px}
.mini .desc{font-size:13px;margin:4px 0 6px}
.mini .stars svg{width:18px;height:18px}
.mini .rec{font-size:13px}
.offer-line{font-size:22px;color:var(--muted)}
.promo{display:flex;align-items:center;text-align:left;border:2px solid var(--rule);margin:0 60px 14px;height:150px;overflow:hidden}
.promo .photo{width:110px;height:110px;margin:0 22px}
.promo-text{flex:1}
.promo-text .name{font-size:24px}
.promo-text .desc{font-size:15px;margin:6px 0}
.promo-text a{font-size:15px;font-weight:700;color:var(--ink);text-decoration:none}
.promo-flag{width:260px;height:100%;position:relative;display:flex;align-items:center;justify-content:center;color:#fff;font-weight:700;font-size:18px}
.promo-flag svg{position:absolute;inset:0;width:100%;height:100%}
.promo-flag span{position:relative;padding-left:40px}
.reach{font-size:18px;color:var(--ink);margin-bottom:6px;text-align:left;padding-left:120px}
</style>
</head>
<body>

<section class="email" style="top:40px;height:560px">
  <div class="social"><span></span><span></span><span></span><span></span></div>
  <div class="brand">velvetlistings-uk.com</div>
  <div class="brand-sub">The Listings Directory</div>
  <p class="lead">Last week this ad was viewed 963 times and produced 135 phone calls for just £49.49pm.</p>
  <div class="listing">
    <div class="photo" role="img" aria-label="Profile photo of the advertiser"></div>
    <div>
      <div class="name">Sienna, 22<small>Birmingham City Centre Escort</small></div>
      <p class="desc">New to Birmingham – Hello there, my name is Sienna, I am from Sweden. My pictures are 100% genuine, I am a glamour model. Call me to arrange a relaxed evening together.</p>
      <div class="rec">RECOMMENDED:
        <span class="stars">
          <svg viewBox="0 0 24 24"><path d="M12 2l3 7h7l-5.5 4.5 2 7.5-6.5-4.5-6.5 4.5 2-7.5L2 9h7z"/></svg>
          <svg viewBox="0 0 24 24"><path d="M12 2l3 7h7l-5.5 4.5 2 7.5-6.5-4.5-6.5 4.5 2-7.5L2 9h7z"/></svg>
          <svg viewBox="0 0 24 24"><path d="M12 2l3 7h7l-5.5 4.5 2 7.5-6.5-4.5-6.5 4.5 2-7.5L2 9h7z"/></svg>
          <svg viewBox="0 0 24 24"><path d="M12 2l3 7h7l-5.5 4.5 2 7.5-6.5-4.5-6.5 4.5 2-7.5L2 9h7z"/></svg>
          <svg viewBox="0 0 24 24"><path d="M12 2l3 7h7l-5.5 4.5 2 7.5-6.5-4.5-6.5 4.5 2-7.5L2 9h7z"/></svg>
        </span>
      </div>
    </div>
  </div>
  <div class="links">Take a look @ <b>www.velvetlistings-uk.com</b><br>Post an ad @ <b>www.velvetlistings-uk.com/post/add</b></div>
</section>

<p class="note">For anything any problem you can view this <u>link</u></p>

<section class="email" style="top:660px;height:570px">
  <div class="social"><span></span><span></span><span></span><span></span></div>
  <div class="brand">velvetlistings-uk.com</div>
  <div class="brand-sub">The Listings Directory</div>
  <div class="bar">Be seen on www.velvetlistings-uk.com</div>
  <div class="pair">
    <div class="bar">Your ad will be seen by 15,000 customers a day</div>
    <div class="bar">See where we are on search engines. Type (your town + escorts) e.g.Birmingham escorts</div>
  </div>
  <div class="links">Post an ad @ <b>www.velvetlistings-uk.com/post/add</b><br>Contact us : <b>support@velvetlistings-uk.com for more information</b> .<br><strong>The VLUK Team.</strong></div>
</section>

<section class="email" style="top:1290px;height:570px">
  <div class="social"><span></span><span></span><span></span><span></span></div>
  <div class="brand">velvetlistings-uk.com</div>
  <div class="brand-sub">The Listings Directory</div>
  <div class="offers">
    <div class="offer">
      <h3>This premium ad on Velvetlistings for 30 days is £54.60</h3>
      <div class="mini">
        <div class="photo" role="img" aria-label="Profile photo of the advertiser"></div>
        <div>
          <div class="name">Sienna, 22<small>Birmingham City Centre</small></div>
          <p class="desc">New to Birmingham, genuine pictures, friendly glamour model available most evenings.</p>
          <div class="rec">RECOMMENDED: <span class="stars"><svg viewBox="0 0 24 24"><path d="M12 2l3 7h7l-5.5 4.5 2 7.5-6.5-4.5-6.5 4.5 2-7.5L2 9h7z"/></svg><svg viewBox="0 0 24 24"><path d="M12 2l3 7h7l-5.5 4.5 2 7.5-6.5-4.5-6.5 4.5 2-7.5L2 9h7z"/></svg><svg viewBox="0 0 24 24"><path d="M12 2l3 7h7l-5.5 4.5 2 7.5-6.5-4.5-6.5 4.5 2-7.5L2 9h7z"/></svg><svg viewBox="0 0 24 24"><path d="M12 2l3 7h7l-5.5 4.5 2 7.5-6.5-4.5-6.5 4.5 2-7.5L2 9h7z"/></svg><svg viewBox="0 0 24 24"><path d="M12 2l3 7h7l-5.5 4.5 2 7.5-6.5-4.5-6.5 4.5 2-7.5L2 9h7z"/></svg></span></div>
        </div>
      </div>
    </div>
    <div class="offer">
      <h3>This premium ad on VLUK for 30 days is £48.49</h3>
      <div class="mini">
        <div class="photo" role="img" aria-label="Profile photo of the advertiser"></div>
        <div>
          <div class="name">Sienna, 22<small>Birmingham City Centre</small></div>
          <p class="desc">New to Birmingham, genuine pictures, friendly glamour model available most evenings.</p>
          <div class="rec">RECOMMENDED: <span class="stars"><svg viewBox="0 0 24 24"><path d="M12 2l3 7h7l-5.5 4.5 2 7.5-6.5-4.5-6.5 4.5 2-7.5L2 9h7z"/></svg><svg viewBox="0 0 24 24"><path d="M12 2l3 7h7l-5.5 4.5 2 7.5-6.5-4.5-6.5 4.5 2-7.5L2 9h7z"/></svg><svg viewBox="0 0 24 24"><path d="M12 2l3 7h7l-5.5 4.5 2 7.5-6.5-4.5-6.5 4.5 2-7.5L2 9h7z"/></svg><svg viewBox="0 0 24 24"><path d="M12 2l3 7h7l-5.5 4.5 2 7.5-6.5-4.5-6.5 4.5 2-7.5L2 9h7z"/></svg><svg viewBox="0 0 24 24"><path d="M12 2l3 7h7l-5.5 4.5 2 7.5-6.5-4.5-6.5 4.5 2-7.5L2 9h7z"/></svg></span></div>
        </div>
      </div>
    </div>
  </div>
  <div class="links">Check out us : <b>www.velvetlistings-uk.com</b><br>Contact us : <b>support@velvetlistings-uk.com for more information</b> .<br><strong>The VLUK Team.</strong></div>
</section>

<section class="email" style="top:1920px;height:670px">
  <div class="social"><span></span><span></span><span></span><span></span></div>
  <div class="brand">velvetlistings-uk.com</div>
  <div class="brand-sub" style="margin-bottom:14px">The Listings Directory</div>
  <div class="bar" style="text-align:center;margin:0 200px 12px;padding:10px">One month free email</div>
  <p class="lead" style="font-size:17px;margin-bottom:10px">In this email we will be offering potential customers their first month free.</p>
  <p class="offer-line" style="margin-bottom:14px">Special Offer – First month free on VLUK – No Credit Card Needed – No Obligation</p>
  <div class="promo">
    <div class="photo" role="img" aria-label="Portrait photo of the featured advertiser"></div>
    <div class="promo-text">
      <div class="name">Dr Ravi Marsh</div>
      <p class="desc">Lorem ipsum dolor sit amet, consectetur adipiscing elit, sed do eiusmod.</p>
      <a>Read More&gt;</a>
    </div>
    <div class="promo-flag">
      <svg viewBox="0 0 260 150" preserveAspectRatio="none"><polygon points="70,0 260,0 260,150 0,150" fill="#ee8a1c"/></svg>
      <span>Add Sections</span>
    </div>
  </div>
  <p class="reach">Be seen by 15,000 people a day – have a look</p>
  <div class="links" style="font-size:18px;line-height:1.5">Check out us : <b>www.velvetlistings-uk.com</b><br>Contact us : <b>support@velvetlistings-uk.com for more information</b> .<br><strong>The VLUK Team.</strong></div>
</section>

</body>
</html>
```